Kestrel Ridge Plumbing Business card & letter head design

We need a new business card and letter head for our plumbing company called kestrel ridge plumbing. attached is the companys logo. We provide domestic and commercial plumbing services in regional western Australia. We are after Something simple yet nice to look at and something that fits within the trade industry.

Target Market(s)

trade/building industry

Contact Information for Business Card

Tarek Holm
Manager
0481 362 714
enquiries@krplumbing.example.au
ABN: 47 153 806 924
PCL: 5318

Domestic & Commercial Plumbing
Tip Truck & Excavator hire

Colors

Designer to choose colors to be used in the design.

```html
<!DOCTYPE html>
<html lang="en">
<head>
<meta charset="utf-8">
<title>Kestrel Ridge Plumbing – Letterhead</title>
<link rel="stylesheet" href="https://fonts.googleapis.com/css2?family=Open+Sans:wght@400;600;700&display=swap">
<style>
  :root {
    --brand-blue: #0b5aa8;
    --brand-grey: #58585b;
    --ink: #2b2b2b;
    --paper: #ffffff;
    --backdrop: #ececec;
    --signature-tone: #e6e9ee;
  }
  * { box-sizing: border-box; margin: 0; padding: 0; }
  html, body { width: 1200px; height: 1012px; overflow: hidden; }
  body {
    background: var(--backdrop);
    font-family: "Open Sans", Arial, sans-serif;
    color: var(--ink);
    position: relative;
  }
  .letterhead {
    position: absolute;
    left: 260px; top: 26px;
    width: 680px; height: 960px;
    background: var(--paper);
    overflow: hidden;
  }
  .header-swoosh { position: absolute; left: 0; top: 0; width: 680px; height: 108px; }
  .brand-name {
    position: absolute; left: 86px; top: 36px;
    font-weight: 700; font-size: 17px; line-height: 1.15;
    color: var(--brand-blue); text-transform: uppercase; letter-spacing: 0.2px;
  }
  .sender { position: absolute; left: 88px; top: 143px; font-size: 10.5px; line-height: 17px; }
  .sender-name { color: var(--brand-blue); font-weight: 600; font-size: 11.5px; }
  .sender-role { font-size: 8.5px; line-height: 14px; }
  .sender-line b { color: var(--brand-blue); font-weight: 700; display: inline-block; width: 20px; }
  .sender-line b.dark { color: var(--ink); }
  .letter-date { position: absolute; right: 88px; top: 193px; font-size: 10.5px; }
  .letter-body { position: absolute; left: 88px; top: 243px; width: 512px; font-size: 10.4px; line-height: 21.5px; }
  .letter-body p { margin-bottom: 21.5px; }
  .sign-off { position: absolute; left: 87px; top: 625px; }
  .signature { width: 96px; height: 28px; background: var(--signature-tone); border-radius: 3px; margin-bottom: 3px; }
  .sign-name { font-weight: 700; font-size: 11px; line-height: 12px; }
  .sign-role { font-size: 11px; line-height: 13px; }
  .contact-strip {
    position: absolute; left: 98px; top: 880px; width: 500px;
    display: flex; justify-content: space-between; align-items: center;
    font-size: 11px; line-height: 13.5px;
  }
  .contact-item { display: flex; align-items: center; gap: 8px; }
  .contact-item svg { width: 27px; height: 27px; flex: none; }
  .contact-item.address { font-weight: 600; }
  .legal-band {
    position: absolute; left: 0; top: 929px; width: 680px; height: 27px;
    background: var(--brand-blue); color: #fff;
    font-size: 7.5px; font-weight: 700;
    display: flex; align-items: center; justify-content: center; gap: 8px;
  }
</style>
</head>
<body>
  <main class="letterhead">
    <svg class="header-swoosh" viewBox="0 0 680 108" preserveAspectRatio="none" aria-hidden="true">
      <polygon points="0,0 155,0 0,46" fill="var(--brand-grey)"/>
      <polygon points="155,0 680,0 680,85 258,20" fill="var(--brand-blue)"/>
      <polygon points="258,22 680,90 680,102" fill="var(--brand-grey)"/>
    </svg>
    <div class="brand-name">Kestrel Ridge<br>Plumbing</div>

    <section class="sender">
      <div class="sender-name">Tarek Holm</div>
      <div class="sender-role">Manager</div>
      <div class="sender-line"><b>A :</b>12 Saltbush Way, Geraldton WA 6530</div>
      <div class="sender-line"><b class="dark">W :</b>enquiries@krplumbing.example.au, krplumbing.example.au</div>
      <div class="sender-line"><b>P :</b>0481 362 714</div>
    </section>
    <div class="letter-date">Date, 10 September, 2020</div>

    <article class="letter-body">
      <p>This is a sample letter that has been placed to demonstrate typing remat (Your Company). letterhead design. When positioned properly, it will serve to work in harmony with all other elements letterhead. This letterhead design is meant to project an image</p>
      <p>This letterhead design is meant project an image of professionalism reliability. By using simple aligen we have created a very spacious feeling. The simplicity suggest rengththe spaciousnes contributes h aesthetics the layout. These basic qualities along with te (Your Company)</p>
      <p>look and helps reinforce the (Your Company) brand. letterhead design is meant to project an image p design. When positioned properly, it will serve to work in harmony all the other elements letterhead. sionalism and reliability.</p>
      <p>This letterhead design is based on the (Form of your logo) form (Your Company) logo. Each stationery we have created a very spacious feeling. The simplicity suggests strength the spaciousnes contribute part of the (Form of your logo).</p>
    </article>

    <section class="sign-off">
      <div class="signature" role="img" aria-label="Handwritten signature of Tarek Holm"></div>
      <div class="sign-name">Tarek Holm</div>
      <div class="sign-role">Manager</div>
    </section>

    <footer class="contact-strip">
      <div class="contact-item phone">
        <svg viewBox="0 0 28 28" aria-hidden="true"><circle cx="14" cy="14" r="14" fill="var(--brand-blue)"/><path d="M10 8.5l2 .2 1 3-1.4 1.2a7 7 0 0 0 3.5 3.5l1.2-1.4 3 1 .2 2c-.3 1-1.2 1.5-2.2 1.4A10 10 0 0 1 8.6 10.7c-.1-1 .4-1.9 1.4-2.2z" fill="#fff"/></svg>
        <span>0481 362 714</span>
      </div>
      <div class="contact-item web">
        <svg viewBox="0 0 28 28" aria-hidden="true"><circle cx="14" cy="14" r="14" fill="var(--brand-grey)"/><g fill="none" stroke="#fff" stroke-width="1.3"><circle cx="14" cy="14" r="6.5"/><ellipse cx="14" cy="14" rx="3" ry="6.5"/><path d="M7.5 14h13"/></g></svg>
        <span>enquiries@krplumbing.example.au<br>krplumbing.example.au</span>
      </div>
      <div class="contact-item address">
        <svg viewBox="0 0 28 28" aria-hidden="true"><circle cx="14" cy="14" r="14" fill="var(--brand-blue)"/><path d="M14 7a4.8 4.8 0 0 0-4.8 4.8c0 3.6 4.8 8.7 4.8 8.7s4.8-5.1 4.8-8.7A4.8 4.8 0 0 0 14 7zm0 6.6a1.8 1.8 0 1 1 0-3.6 1.8 1.8 0 0 1 0 3.6z" fill="#fff"/></svg>
        <span>88 Marine Terrace<br>Geraldton, WA 6530</span>
      </div>
    </footer>

    <div class="legal-band"><span>ABN: 47 153 806 924</span><span>|</span><span>PCL: 5318</span></div>
  </main>
</body>
</html>
```